Re-design of Business Card

We require a design for our business card.

Korrim is a supplier of industrial packaging specializing in plastic products. We are undergoing a rebranding to appear more corporate. We have changed our company name to korrim and have a new logo.

I have uploaded our old card design with the previous company name.
Don't copy the current design. We are looking for a new design.

Industry/Entity Type

Manufacturing

Contact Information for Business Card

please don't copy the current design. we are looking for a new design.

Font styles to use
Sans Serif

Colors

Designer to choose colors to be used in the design.

Requirements
Must have
• clean and easy to read.

```html
<!DOCTYPE html>
<html lang="en">
<head>
<meta charset="utf-8">
<title>Korrim Business Card</title>
<link href="https://fonts.googleapis.com/css2?family=Montserrat:wght@400;500;600;700;800&display=swap" rel="stylesheet">
<style>
  :root {
    --brand-orange: #f47b20;
    --ink: #1f1f1f;
    --muted: #8a8a8a;
    --paper: #ffffff;
    --backdrop: #d8cfc2;
  }
  * { margin: 0; padding: 0; box-sizing: border-box; }
  html, body { width: 1200px; height: 900px; overflow: hidden; }
  body {
    background: var(--backdrop);
    font-family: "Montserrat", Arial, sans-serif;
    position: relative;
  }
  .card {
    position: absolute;
    left: 311px;
    width: 577px;
    height: 329px;
    box-shadow: 0 6px 14px rgba(0,0,0,0.18);
  }
  /* Front */
  .card-front {
    top: 98px;
    background: var(--brand-orange);
    color: var(--paper);
    text-align: center;
  }
  .front-wordmark {
    position: absolute;
    top: 96px;
    left: 0; right: 0;
    font-size: 64px;
    font-weight: 700;
    letter-spacing: 1px;
    line-height: 1;
  }
  .front-services {
    position: absolute;
    top: 194px;
    left: 0; right: 0;
    font-size: 14px;
    font-weight: 500;
    letter-spacing: 0.4px;
    line-height: 20px;
  }
  /* Back */
  .card-back {
    top: 472px;
    background: var(--paper);
  }
  .person {
    position: absolute;
    right: 297px;
    top: 74px;
    text-align: right;
  }
  .back-wordmark {
    font-size: 48px;
    font-weight: 700;
    color: var(--brand-orange);
    line-height: 1;
    letter-spacing: 1px;
    margin-bottom: 18px;
  }
  .person-name {
    font-size: 18px;
    font-weight: 700;
    color: var(--brand-orange);
    letter-spacing: 0.3px;
    line-height: 20px;
  }
  .person-role {
    font-size: 13px;
    color: var(--muted);
    line-height: 18px;
    margin-bottom: 7px;
  }
  .contact-line {
    display: flex;
    justify-content: flex-end;
    align-items: center;
    gap: 8px;
    font-size: 15px;
    color: var(--ink);
    line-height: 22px;
  }
  .divider {
    position: absolute;
    left: 304px;
    top: 77px;
    width: 2px;
    height: 154px;
    background: var(--brand-orange);
  }
  .office {
    position: absolute;
    left: 331px;
    top: 76px;
  }
  .office-title {
    font-size: 14px;
    font-weight: 700;
    color: var(--brand-orange);
    letter-spacing: 0.4px;
    line-height: 18px;
    margin-bottom: 3px;
  }
  .office-address {
    font-size: 15px;
    color: var(--muted);
    line-height: 19.5px;
    letter-spacing: 0.4px;
    font-style: normal;
    margin-bottom: 12px;
  }
  .office-line {
    display: flex;
    align-items: center;
    gap: 8px;
    font-size: 15px;
    color: var(--ink);
    line-height: 22px;
  }
  .icon { width: 15px; height: 15px; flex: none; fill: var(--brand-orange); }
  .credentials-band {
    position: absolute;
    left: 0; right: 0; bottom: 0;
    height: 49px;
    background: var(--brand-orange);
    color: var(--paper);
    font-size: 14px;
    font-weight: 500;
    display: flex;
    align-items: center;
    justify-content: center;
  }
</style>
</head>
<body>

<section class="card card-front">
  <div class="front-wordmark">KORRIM</div>
  <p class="front-services">
    PALLET CONTAINMENT &nbsp;|&nbsp; FLEXIBLE PACKAGING<br>
    PALLET WRAPPING MACHINERY &nbsp;|&nbsp; GENERAL PACKAGING
  </p>
</section>

<section class="card card-back">
  <div class="person">
    <div class="back-wordmark">KORRIM</div>
    <div class="person-name">DANA WHITFORD</div>
    <div class="person-role">Machinery Sales Manager</div>
    <div class="contact-line">12 804 3356
      <svg class="icon" viewBox="0 0 16 16"><path d="M3.6 1.2l2.3 2.6-1.3 1.9c.9 2 2.6 3.7 4.6 4.6l1.9-1.3 2.6 2.3-1.2 2.1C7.3 15 1 8.7 1.4 2.4z"/></svg>
    </div>
    <div class="contact-line">dana@korrim.com.au
      <svg class="icon" viewBox="0 0 16 16"><path d="M1 3h14v1.5L8 9 1 4.5z"/><path d="M1 6.2l7 4.5 7-4.5V13H1z"/></svg>
    </div>
  </div>

  <div class="divider"></div>

  <div class="office">
    <div class="office-title">HEAD OFFICE</div>
    <address class="office-address">48 Harlow Street<br>Ridgeview, Qld<br>4120 Australia</address>
    <div class="office-line">
      <svg class="icon" viewBox="0 0 16 16"><path d="M3.6 1.2l2.3 2.6-1.3 1.9c.9 2 2.6 3.7 4.6 4.6l1.9-1.3 2.6 2.3-1.2 2.1C7.3 15 1 8.7 1.4 2.4z"/></svg>
      1300 418 627
    </div>
    <div class="office-line">
      <svg class="icon" viewBox="0 0 16 16"><rect x="4" y="1" width="8" height="4"/><rect x="1" y="6" width="14" height="6" rx="1"/><rect x="4" y="10" width="8" height="5" fill="#fff" stroke="#f47b20" stroke-width="1.2"/></svg>
      +61 7 3540 2917
    </div>
    <div class="office-line">
      <svg class="icon" viewBox="0 0 16 16"><circle cx="8" cy="8" r="7"/><path d="M1 8h14M8 1c-3 3-3 11 0 14M8 1c3 3 3 11 0 14" stroke="#fff" stroke-width="1.1" fill="none"/></svg>
      www.korrim.com.au
    </div>
  </div>

  <div class="credentials-band">Distribution Throughout AUS &amp; NZ | HACCP Certified | ISO 9001</div>
</section>

</body>
</html>
```